Destination Wedding Photographer

I am a Wedding photographer based in San Juan, Puerto Rico. The banner will be shown in the United States to brides that plan to have their wedding in Puerto Rico.

I want to highlight the following words/phrases
Puerto Rico
Destination Wedding
Photographer
(in that order)

feel free to get creative adding your own inspired text.

My web site: www.benitolavarro.com

Target Market(s)

Brides in the united states looking for a photographer for their wedding in Puerto Rico

Industry/Entity Type

Wedding

Requirements
Must have
• + Your ad must be a .gif, .png or .jpg smaller than 40kb in filesize
+ include the following sizes: 300x250, 728x90, 160x600, 468x60, or 120x600
+ Your ad must include the advertiser's brand
+ Your ad must have a border
Should not have
• + Your ad cannot imitate computer effects like scrolling or mousing over
+ No animations longer than 30 seconds
+ No strobe or flashing effects allowed
+ Your ad and campaign must not feature or promote alcohol, anabolic steroids, drugs, financial products, gambling, adult content, or weight loss products

```html
<!DOCTYPE html>
<html lang="en">
<head>
<meta charset="utf-8">
<title>Puerto Rico Destination Wedding Photographer – Banner Set</title>
<link rel="stylesheet" href="https://fonts.googleapis.com/css2?family=Oswald:wght@400;500;600;700&display=swap">
<style>
  :root{
    --stage:#e8e5e1;
    --panel:#2a2623;
    --panel-light:#37322d;
    --frame:#141210;
    --gold-top:#ffd84d;
    --gold-bottom:#f29e00;
    --white:#ffffff;
    --ink:#1a1a1a;
    --btn-top:#ffe257;
    --btn-bottom:#f4b000;
    --silver:#c9c9c9;
    --sky:#7fa6c4;
    --skin:#d9a98a;
    --dress:#f3f1ee;
    --suit:#e9e4da;
  }
  *{box-sizing:border-box;margin:0;padding:0}
  html,body{width:1200px;height:799px;overflow:hidden}
  body{background:var(--stage);position:relative;font-family:"Oswald",sans-serif}

  .banner{
    position:absolute;overflow:hidden;
    background:radial-gradient(ellipse at 40% 40%,var(--panel-light),var(--panel) 70%);
    border:1px solid var(--frame);
  }
  .banner--skyscraper{left:31px;top:33px;width:196px;height:734px}
  .banner--rect-a{left:252px;top:151px;width:368px;height:305px}
  .banner--rect-b{left:642px;top:151px;width:368px;height:305px}
  .banner--small-leaderboard{left:252px;top:503px;width:574px;height:70px}
  .banner--leaderboard{left:252px;top:601px;width:891px;height:109px}

  .photo{
    position:absolute;
    background:linear-gradient(100deg,var(--sky) 0%,var(--skin) 30%,var(--dress) 48%,var(--skin) 66%,var(--suit) 85%,var(--sky) 100%);
  }
  .banner--skyscraper .photo{left:0;top:0;width:196px;height:300px;
    clip-path:path('M0 0 H196 V248 Q110 262 0 300 Z')}
  .banner--rect-a .photo,.banner--rect-b .photo{left:145px;top:0;width:223px;height:305px;
    clip-path:path('M26 0 H223 V305 H12 Q-8 150 26 0 Z')}
  .banner--small-leaderboard .photo{left:0;top:0;width:192px;height:70px;
    clip-path:path('M0 0 H182 Q196 35 186 70 H0 Z')}
  .banner--leaderboard .photo{left:0;top:0;width:310px;height:109px;
    clip-path:path('M0 0 H292 Q312 55 298 109 H0 Z')}

  .swoosh{position:absolute;left:0;top:0;pointer-events:none}

  .line{position:absolute;line-height:1;text-align:center;white-space:nowrap;text-transform:uppercase}
  .line--gold{
    font-weight:700;
    background:linear-gradient(var(--gold-top),var(--gold-bottom));
    -webkit-background-clip:text;background-clip:text;color:transparent;
  }
  .line--white{color:var(--white);font-weight:500}

  .brand{position:absolute;line-height:1;text-align:center;color:var(--white);font-weight:400;white-space:nowrap}

  .cta{
    position:absolute;display:flex;align-items:center;justify-content:center;gap:6px;
    background:linear-gradient(var(--btn-top),var(--btn-bottom));
    border-radius:4px;color:var(--ink);font-weight:500;line-height:1;
    box-shadow:0 1px 2px rgba(0,0,0,.5);
  }
  .cta svg{flex:none}
</style>
</head>
<body>

<!-- 160x600 skyscraper -->
<div class="banner banner--skyscraper">
  <div class="photo" role="img" aria-label="Photo of a laughing bride and groom by the sea"></div>
  <svg class="swoosh" width="196" height="310" viewBox="0 0 196 310"><path d="M196 246 Q110 260 0 298" fill="none" stroke="var(--silver)" stroke-width="3"/></svg>
  <div class="line line--gold" style="left:0;width:196px;top:296px;font-size:56px">Puerto</div>
  <div class="line line--gold" style="left:0;width:196px;top:348px;font-size:80px">Rico</div>
  <div class="line line--white" style="left:0;width:196px;top:458px;font-size:33px">Destination</div>
  <div class="line line--white" style="left:0;width:196px;top:498px;font-size:44px">Wedding</div>
  <div class="line line--white" style="left:0;width:196px;top:551px;font-size:27px">Photographer</div>
  <div class="brand" style="left:0;width:196px;top:622px;font-size:26px">Benito Lavarro</div>
  <div class="cta" style="left:18px;top:685px;width:159px;height:39px;font-size:17px">Learn More!
    <svg width="22" height="22" viewBox="0 0 22 22"><circle cx="11" cy="11" r="11" fill="var(--ink)"/><path d="M9 6 L14 11 L9 16" fill="none" stroke="var(--white)" stroke-width="2.5"/></svg>
  </div>
</div>

<!-- 300x250 rectangle A -->
<div class="banner banner--rect-a">
  <div class="photo" role="img" aria-label="Photo of a laughing bride and groom by the sea"></div>
  <svg class="swoosh" width="368" height="305" viewBox="0 0 368 305"><path d="M171 0 Q137 150 157 305" fill="none" stroke="var(--silver)" stroke-width="3"/></svg>
  <div class="line line--gold" style="left:0;width:170px;top:5px;font-size:46px">Puerto</div>
  <div class="line line--gold" style="left:0;width:170px;top:49px;font-size:66px">Rico</div>
  <div class="line line--white" style="left:0;width:170px;top:137px;font-size:28px">Destination</div>
  <div class="line line--white" style="left:0;width:170px;top:165px;font-size:37px">Wedding</div>
  <div class="line line--white" style="left:0;width:170px;top:210px;font-size:22px">Photographer</div>
  <div class="brand" style="left:0;width:170px;top:256px;font-size:22px">Benito Lavarro</div>
  <div class="cta" style="left:191px;top:260px;width:154px;height:39px;font-size:17px">Learn More!
    <svg width="22" height="22" viewBox="0 0 22 22"><circle cx="11" cy="11" r="11" fill="var(--ink)"/><path d="M9 6 L14 11 L9 16" fill="none" stroke="var(--white)" stroke-width="2.5"/></svg>
  </div>
</div>

<!-- 300x250 rectangle B -->
<div class="banner banner--rect-b">
  <div class="photo" role="img" aria-label="Photo of a laughing bride and groom by the sea"></div>
  <svg class="swoosh" width="368" height="305" viewBox="0 0 368 305"><path d="M171 0 Q137 150 157 305" fill="none" stroke="var(--silver)" stroke-width="3"/></svg>
  <div class="line line--gold" style="left:0;width:170px;top:5px;font-size:46px">Puerto</div>
  <div class="line line--gold" style="left:0;width:170px;top:49px;font-size:66px">Rico</div>
  <div class="line line--white" style="left:0;width:170px;top:137px;font-size:28px">Destination</div>
  <div class="line line--white" style="left:0;width:170px;top:165px;font-size:37px">Wedding</div>
  <div class="line line--white" style="left:0;width:170px;top:210px;font-size:22px">Photographer</div>
  <div class="brand" style="left:0;width:170px;top:256px;font-size:22px">Benito Lavarro</div>
  <div class="cta" style="left:191px;top:260px;width:154px;height:39px;font-size:17px">Learn More!
    <svg width="22" height="22" viewBox="0 0 22 22"><circle cx="11" cy="11" r="11" fill="var(--ink)"/><path d="M9 6 L14 11 L9 16" fill="none" stroke="var(--white)" stroke-width="2.5"/></svg>
  </div>
</div>

<!-- 468x60 small leaderboard -->
<div class="banner banner--small-leaderboard">
  <div class="photo" role="img" aria-label="Photo of a laughing bride and groom by the sea"></div>
  <svg class="swoosh" width="574" height="70" viewBox="0 0 574 70"><path d="M182 0 Q196 35 186 70" fill="none" stroke="var(--silver)" stroke-width="2"/></svg>
  <div class="line line--gold" style="left:213px;width:233px;top:5px;font-size:40px">Puerto Rico</div>
  <div class="line line--white" style="left:213px;width:233px;top:48px;font-size:15px">Destination Wedding Photographer</div>
  <div class="brand" style="left:466px;width:100px;top:12px;font-size:16px">Benito Lavarro</div>
  <div class="cta" style="left:472px;top:43px;width:92px;height:21px;font-size:11px;gap:4px">Learn More!
    <svg width="13" height="13" viewBox="0 0 22 22"><circle cx="11" cy="11" r="11" fill="var(--ink)"/><path d="M9 6 L14 11 L9 16" fill="none" stroke="var(--white)" stroke-width="3"/></svg>
  </div>
</div>

<!-- 728x90 leaderboard -->
<div class="banner banner--leaderboard">
  <div class="photo" role="img" aria-label="Photo of a laughing bride and groom by the sea"></div>
  <svg class="swoosh" width="891" height="109" viewBox="0 0 891 109"><path d="M292 0 Q312 55 298 109" fill="none" stroke="var(--silver)" stroke-width="3"/></svg>
  <div class="line line--gold" style="left:332px;width:362px;top:8px;font-size:62px">Puerto Rico</div>
  <div class="line line--white" style="left:332px;width:362px;top:73px;font-size:26px">Destination Wedding Photographer</div>
  <div class="brand" style="left:730px;width:150px;top:22px;font-size:24px">Benito Lavarro</div>
  <div class="cta" style="left:738px;top:66px;width:140px;height:37px;font-size:16px">Learn More!
    <svg width="20" height="20" viewBox="0 0 22 22"><circle cx="11" cy="11" r="11" fill="var(--ink)"/><path d="M9 6 L14 11 L9 16" fill="none" stroke="var(--white)" stroke-width="2.5"/></svg>
  </div>
</div>

</body>
</html>
```